Mobile Repair Service on location needs a Web Design

We are starting a new mobile device repair service called Gadget Haven and our website needs a design!

Hello Designers!
First, we'd like to make clear this is more than a simple web design contest, we want the designers to create an idea. We want someone who can create the whole theme of the service's we provide. We want someone that can help design our visual branding, help us communicate a sentiment. And we are willing to pay for that.

Who are we?
Our company is based in Rotterdam, the Netherlands. We provide different services for all kinds of electronic devices. The kind of services we provide are, among other things, installations of hardware and software and the repair of broken or malfunctioning devices.
We are starting a new service that offers mobile device repairs on location, be it at the home of our customers, their office, or any other place. Just give us the address and we will come to you for the repair job. This is also our main USP. We have multiple skilled engineers who drive trough the country on a daily basis and can be on location within a working day. Repair is done immediately onsite while the customer waits. At this stage we will start with the smartphone product-group within the mobile devices. In a second phase we might also add tablets.
People don't want to be without their phone for weeks because of some parts that needed to be ordered by a repair center they had to sent their phone to. We offer a fully functional mobile repair center in the form of specially customized vans. These vans have all the tools and utilities needed by our engineers to safely repair your mobile device. Your phone is being repaired directly in front of you, the next business-day, on a location you desire.

For this new service we are creating a website called Gadget Haven. The website needs a story and matching design and this is where you come in. We are not looking for a simple template design we can get from any place. We need a story. We want you to create an idea, build a unique theme or vision that helps sell the product/service. This goes beyond the design of the website. We need the whole package, the design you are creating needs to have returning elements like icons, color use, images, maybe even characters etc. You name it! There needs to be a common thread in the design so we can reuse elements in, for example, the email templates, the work order or receipt we give to our customers (we may contact the winner of the contest to design these for us as well!).

The name 'Gadget Haven' is chosen. Haven (short for rehabilitate) has a bold and playful tone to it and the design needs to reflect the name. So we're looking for a somewhat playful and cheeky design. Definitely not too serious and definitely modern. We already got a logo that we love and that fit's this description (see attached design documents for the logo). It's bold, powerful and fun. Our web design needs to reflect this as well and has to fit in with our logo.
We would really like it if the design somehow incorporates elements that highlight our unique selling points (repairs on location, we come to you etc.). We would really like some form of story telling in the design. Think clumsy people breaking their phones. Teenagers in tears because they have no access to their friends. People nowadays have the need to always be 'connected'. What happens when your phone is broken or malfunctioning? We're handling tech, we are nerds and a little bit weird, but we're professionals and here to help you with your problem. The sentiment Wire Troop tries to communicate is something we really like. We're looking for fresh idea's, anything goes!

In an overview all Unique Selling Points of the Gadget haven service:
- Professional service on location. Don’t ship to us we will come to you!
- Clear pricing upfront. No hidden cost.
- Next business-day repair.
- Backed by a professional call center open 12 hours a day and open on a Saturday as well
- Backed by a professional repair center with more then 12 years of experience
- Repair is done by certified engineers
- 1 year warranty on the repair

The process:
The main function of our website will be for customers to make a repair request. A customer will visit our website and can make a repair request immediately by going through a 'request-order-flow'. In this flow he or she will need to fill in some forms and can select wich type/model/brand of mobile device he or she has and what parts need to be repaired. After a request is placed we will call the customer back (within an hour) for a short intake and to set a date/time and location. Our engineer will meet the customer at the specified location and will repair the device onsite in one of our mobile repair centers, which is a specialized van equipped with all the tools needed for device restorations.
So in short the steps are:
- Choose your device and repair job
- Place the order
- Get a callback within the hour
- Set date and location
- We will come to you.

Website functionality:
Our website is our main form of communication. So the sentiment we want to communicate needs be reflected in the design. We need a main/front page designed (preferably a long scrolling page design) containing:
1. Customers will be able to request a repair job directly on our website. So there will need to be a prominent button/link at the top of our main page that will bring the customer to this 'request-order-flow'. This is the main flow which needs to be full focus on the front page. All other items are secondary.
2. The general information of who we are and what we do, and why the customer should choose us. Preferably in short bullet-point type keywords/sentences with icons or other visual cues. See our unique selling points to get an idea of the information that will be displayed here.
3. There needs to be a section that will explain the process (see above) of a repair request step-by- step, again in brief short key sentences and with (custom) icons.
4. There needs to be a section that explains to the customer he/she can always contact us if they are not sure what the problem is with their device, and for this reason are not sure what repair request they should order.
5. We want to implement some functionality that display customer ratings or customer reviews. So there needs to be room for some kind of widget of plugin we're going to implement which shows these reviews.
6. A 'For business section' where we will explain all the options we provide for corporate clients.
7. Social media links.
8. There needs to be a menu with buttons that leads to the all sections described in the previous points.

For now, we need a design for our front page. In the second phase, when we have picked our winner, we may ask the winner to design the page(s) for our request workflow as well.

EDIT:
Finally, we have a very specific order in mind for the different segments of our website. We would like you to add some more segments that were not in our original brief as well:

1. Top header with order/request button. (should instantly make clear our main USP, we do repairs on location)
2. Our process
3. Our unique selling points / why choose us
4. The kind of repairs we do (broken screens, broken batteries, water damage, broken camera's, no sound etc.)
5. A 'meet our team' section, where we introduce some of our engineers
6. A 'contact us for any questions' section/
7. Testimonials/user reviews
8. A section where we show key performance indicators
9. 'For businesses' sections
10.'Subscribe for newsletter' field
11. Social media buttons

Industry/Entity Type

It Service

Number of Pages Required

1 page

Font styles to use
Sans Serif

Requirements
Must have
• a main/front page, design only
• custom icons/images for banners, adverts online and in print (high res)
Nice to have
• Storytelling in our design.
• Design that fits with our brand new logo.
• Elements like icons to have a flat design.
• Keep in mind that the website will need to be responsive when designing! (Ideally provide an example of the mobile design as well)
• Create a fun and trustworthy feeling.

```html
<!DOCTYPE html>
<html lang="en">
<head>
<meta charset="utf-8">
<title>Gadget Haven – Mobile Repair On Location</title>
<link href="https://fonts.googleapis.com/css2?family=Dosis:wght@500;600;700;800&family=Open+Sans:wght@400;600;700&display=swap" rel="stylesheet">
<style>
:root{
  --red:#e7232b;
  --red-deep:#c9181f;
  --purple:#5b2a8c;
  --purple-bubble:#4a2683;
  --yellow:#ffe500;
  --orange:#f26522;
  --ink:#3b3b3b;
  --muted:#8a8a8a;
  --line:#d9d9d9;
  --white:#ffffff;
}
*{box-sizing:border-box;margin:0;padding:0}
html,body{width:1200px;height:2308px;overflow:hidden;background:var(--white)}
body{font-family:"Open Sans",sans-serif;color:var(--ink)}
.page{position:relative;width:1200px;height:2308px;overflow:hidden}

/* hero */
.hero{position:absolute;left:0;top:0;width:1200px;height:620px;background:var(--red)}
.hero__backdrop{position:absolute;left:780px;top:0;width:420px;height:620px;
  background:linear-gradient(180deg,rgba(150,10,20,0) 0%,rgba(150,10,20,.12) 55%,rgba(150,10,20,.22) 100%)}
.brand{position:absolute;left:228px;top:16px;display:flex;align-items:center;gap:10px}
.brand__mark{width:30px;height:30px;background:var(--white);border-radius:50%}
.brand__name{font-family:"Dosis",sans-serif;font-weight:800;font-size:20px;line-height:20px;color:var(--white);letter-spacing:.5px}
.brand__tag{font-family:"Dosis",sans-serif;font-weight:800;font-size:9px;color:var(--white);letter-spacing:.5px;margin-top:2px}
.nav{position:absolute;left:612px;top:38px;display:flex;gap:24px;align-items:center}
.nav a{font-family:"Dosis",sans-serif;font-weight:700;font-size:11px;color:var(--white);text-decoration:none;letter-spacing:.6px}
.nav__burger{width:16px;height:12px;border-top:2px solid var(--white);border-bottom:2px solid var(--white);position:relative}
.nav__burger::after{content:"";position:absolute;left:0;right:0;top:3px;border-top:2px solid var(--white)}
.cta{position:absolute;left:500px;top:142px;width:200px;height:34px;border-radius:17px;background:var(--yellow);
  font-family:"Dosis",sans-serif;font-weight:800;font-size:14px;color:#1c1c1c;letter-spacing:.6px;
  display:flex;align-items:center;justify-content:center;box-shadow:0 4px 10px rgba(0,0,0,.15)}
.hero__device{position:absolute;left:368px;top:196px;width:300px;height:300px;border-radius:50%;
  border:8px solid var(--white);background:radial-gradient(circle at 45% 45%,#4a4f57 0%,#23262b 60%,#e9e9e9 62%,#f5f5f5 100%)}
.bubble{position:absolute;left:640px;top:244px;width:150px;height:110px;border-radius:55px;background:var(--purple-bubble);
  color:var(--white);font-family:"Dosis",sans-serif;font-weight:700;font-size:17px;line-height:20px;
  display:flex;align-items:center;justify-content:center;text-align:center;padding:0 18px}
.bubble::before{content:"";position:absolute;left:-10px;top:60px;border:10px solid transparent;border-right:14px solid var(--purple-bubble)}
.slider-dots{position:absolute;left:1148px;top:226px;display:flex;flex-direction:column;gap:8px}
.slider-dots i{display:block;width:6px;height:6px;border-radius:50%;background:rgba(255,255,255,.5)}
.slider-dots i.on{background:var(--white)}

/* why us */
.tag{display:inline-block;background:var(--orange);color:var(--white);font-family:"Dosis",sans-serif;font-weight:700;
  font-size:10px;letter-spacing:.6px;padding:3px 10px}
.why__tag{position:absolute;left:0;width:1200px;top:632px;text-align:center}
.why__title{position:absolute;left:0;width:1200px;top:652px;text-align:center;font-family:"Dosis",sans-serif;font-weight:700;
  font-size:36px;color:var(--ink);letter-spacing:.5px}
.why__axis{position:absolute;left:599px;top:710px;width:2px;height:300px;background:var(--line)}
.why__node{position:absolute;left:588px;top:778px;width:24px;height:24px;border-radius:50%;background:var(--white);border:6px solid var(--line)}
.why__art{position:absolute;height:240px;background:linear-gradient(180deg,#f7f7f7,#e4e4e4);border-radius:6px}
.why__art--who{left:250px;top:760px;width:200px}
.why__art--what{left:690px;top:770px;width:220px}
.feature{position:absolute;width:330px}
.feature--who{left:228px;top:1022px}
.feature--what{left:680px;top:1022px}
.feature h3{font-family:"Dosis",sans-serif;font-weight:600;font-size:36px;color:var(--ink);letter-spacing:.5px;line-height:42px}
.feature p{font-size:12px;line-height:18px;color:var(--muted);margin-top:8px;width:310px}
.feature .more{display:inline-block;margin-top:12px;font-size:10px;color:var(--muted);border:1px solid var(--line);padding:3px 12px;border-radius:10px}

/* process */
.process{position:absolute;left:0;top:1280px;width:1200px;height:1028px}
.process svg.bg{position:absolute;left:0;top:0}
.process__tag{position:absolute;left:0;width:1200px;top:40px;text-align:center}
.process__title{position:absolute;left:0;width:1200px;top:58px;text-align:center;font-family:"Dosis",sans-serif;font-weight:700;
  font-size:34px;color:var(--white);letter-spacing:.8px}
.step{position:absolute;color:var(--white)}
.step h4{font-family:"Dosis",sans-serif;font-weight:700;font-size:32px;line-height:36px}
.step p{font-size:11px;line-height:16px;color:rgba(255,255,255,.85);margin-top:8px;width:250px}
.step-icon{position:absolute}
</style>
</head>
<body>
<div class="page">

  <header class="hero">
    <div class="hero__backdrop" role="img" aria-label="Faint city landmark in the hero background"></div>
    <div class="brand">
      <span class="brand__mark"></span>
      <div>
        <div class="brand__name">GADGET<br>HAVEN</div>
        <div class="brand__tag">Repair on location</div>
      </div>
    </div>
    <nav class="nav">
      <a href="#">HOME</a><a href="#">REPAIR</a><a href="#">FEATURES</a><a href="#">SERVICES</a><a href="#">CONTACT US</a>
      <span class="nav__burger"></span>
    </nav>
    <div class="cta">REQUEST ORDER FLOW</div>
    <div class="hero__device" role="img" aria-label="Hand holding an opened smartphone showing its internal components"></div>
    <div class="bubble">Repairs on location, we come to you...</div>
    <div class="slider-dots"><i class="on"></i><i></i><i></i></div>
  </header>

  <section class="why">
    <div class="why__tag"><span class="tag">WHY THE CUSTOMER</span></div>
    <h2 class="why__title">SHOULD CHOOSE US</h2>
    <div class="why__axis"></div>
    <div class="why__node"></div>
    <div class="why__art why__art--who" role="img" aria-label="Isometric line drawing of two smartphones side by side"></div>
    <div class="why__art why__art--what" role="img" aria-label="Isometric line drawing of a wrench on a platform"></div>
    <div class="feature feature--who">
      <h3>WHO WE ARE</h3>
      <p>We are a crew of certified engineers who fix smartphones on the spot, wherever you happen to be today.</p>
      <span class="more">Read more</span>
    </div>
    <div class="feature feature--what">
      <h3>WHAT WE DO</h3>
      <p>We replace screens, batteries and cameras inside our mobile repair vans while you wait right beside us.</p>
      <span class="more">Read more</span>
    </div>
  </section>

  <section class="process">
    <svg class="bg" width="1200" height="1028" viewBox="0 0 1200 1028">
      <rect width="1200" height="1028" fill="var(--red)"/>
      <path d="M0 0 H820 C780 220 560 450 0 500 Z" fill="var(--purple)"/>
      <path d="M0 780 C260 800 520 930 640 1028 H0 Z" fill="var(--purple)"/>
      <g fill="none" stroke="rgba(255,255,255,.6)" stroke-width="2" stroke-dasharray="6 6">
        <path d="M560 270 C620 300 660 330 690 350"/>
        <path d="M650 410 C580 440 480 455 410 462"/>
        <path d="M610 560 C630 610 650 650 662 690"/>
        <path d="M640 790 C540 840 420 870 350 900"/>
      </g>
      <g fill="none" stroke="rgba(255,255,255,.8)" stroke-width="2">
        <path d="M684 344 l8 8 -11 2"/><path d="M418 456 l-9 6 9 5"/>
        <path d="M654 684 l8 8 2 -11"/><path d="M358 893 l-9 8 11 2"/>
      </g>
    </svg>
    <div class="process__tag"><span class="tag">OUR</span></div>
    <h2 class="process__title">PROCESS</h2>

    <svg class="step-icon" style="left:222px;top:126px" width="90" height="100" viewBox="0 0 90 100" fill="none" stroke="#fff" stroke-width="2.5">
      <rect x="6" y="14" width="36" height="66" rx="6" transform="rotate(-10 24 47)"/>
      <rect x="42" y="10" width="36" height="66" rx="6" stroke="var(--orange)" transform="rotate(8 60 43)"/>
      <circle cx="60" cy="68" r="3" stroke="var(--orange)"/>
    </svg>
    <div class="step" style="left:366px;top:140px">
      <h4>Choose Your device<br>and repair job</h4>
      <p>Pick your phone model and tell us which part needs a fix in a few simple clicks.</p>
    </div>

    <svg class="step-icon" style="left:688px;top:294px" width="80" height="80" viewBox="0 0 80 80" fill="none" stroke="#fff" stroke-width="2.5">
      <path d="M6 30 L26 22 L46 30 L70 22 V70 L46 76 L26 68 L6 76 Z"/>
      <path d="M46 8 a12 12 0 0 1 12 12 c0 10 -12 22 -12 22 s-12 -12 -12 -22 a12 12 0 0 1 12 -12 z" stroke="var(--orange)"/>
      <circle cx="46" cy="20" r="4" stroke="var(--orange)"/>
    </svg>
    <div class="step" style="left:790px;top:306px">
      <h4>Place the order</h4>
      <p>Confirm your request online and receive a clear price upfront with no hidden costs.</p>
    </div>

    <svg class="step-icon" style="left:232px;top:480px" width="80" height="80" viewBox="0 0 80 80" fill="none" stroke="#fff" stroke-width="2.5">
      <path d="M14 18 c6 -6 12 -6 16 0 l6 10 c2 4 0 8 -4 10 c2 8 8 14 16 16 c2 -4 6 -6 10 -4 l10 6 c6 4 6 10 0 16 c-10 10 -30 2 -44 -12 c-14 -14 -20 -32 -10 -42 z" stroke="var(--orange)"/>
      <path d="M46 10 a24 24 0 0 1 24 24"/><path d="M46 20 a14 14 0 0 1 14 14"/>
    </svg>
    <div class="step" style="left:330px;top:480px">
      <h4>Get a Callback<br>within the hour</h4>
      <p>Our call center phones you back within an hour for a short intake.</p>
    </div>

    <svg class="step-icon" style="left:664px;top:694px" width="96" height="90" viewBox="0 0 96 90" fill="none" stroke="#fff" stroke-width="2.5">
      <rect x="4" y="14" width="66" height="62" rx="4"/>
      <path d="M4 30 H70"/><path d="M18 6 V20 M56 6 V20"/>
      <path d="M16 42h8M32 42h8M48 42h8M16 56h8M32 56h8M48 56h8"/>
      <path d="M80 50 a10 10 0 0 1 10 10 c0 8 -10 18 -10 18 s-10 -10 -10 -18 a10 10 0 0 1 10 -10 z" stroke="var(--orange)"/>
    </svg>
    <div class="step" style="left:790px;top:708px">
      <h4>Set date and<br>location</h4>
      <p>Choose the day, time and place that suits you best for the repair.</p>
    </div>

    <svg class="step-icon" style="left:230px;top:900px" width="100" height="100" viewBox="0 0 100 100" fill="none" stroke="#fff" stroke-width="2.5">
      <path d="M20 10 a20 20 0 0 0 22 30 l40 40 a8 8 0 0 0 10 -10 l-40 -40 a20 20 0 0 0 -30 -22 l12 12 -4 10 -10 4 z" stroke="var(--orange)"/>
      <rect x="62" y="10" width="26" height="44" rx="4"/>
    </svg>
    <div class="step" style="left:372px;top:940px">
      <h4>We will come to You</h4>
      <p>Our engineer arrives in a fully equipped van and repairs your phone onsite.</p>
    </div>
  </section>

</div>
</body>
</html>
```